We need a poster design for "KEVO Sports Night" events. The events have been around for 3 years and we hope the poster will give a sense of vibrant and active designs. It is more to a community event with teamwork and fun.

I have uploaded a past event poster just FYI.

Target Market(s)

Community, Family

Industry/Entity Type

Non Profit

Logo Text

KEVO Sports Night

Requirements
Must have
• KEVO Sports Night
• Organiser: KEVO Sydney
• Date: 25/11/2017
• Time: 4:00pm
• Venue: Wendamere Park
• Friendbook: kevosport

```html
<!DOCTYPE html>
<html lang="en">
<head>
<meta charset="utf-8">
<title>KEVO Sports Night</title>
<link rel="stylesheet" href="https://fonts.googleapis.com/css2?family=Cabin:wght@700&family=Zilla+Slab:wght@700&display=swap">
<style>
  :root {
    --navy: #0a0f6e;
    --sky: #8d96c8;
    --paper: #ffffff;
    --banner: #f57a1f;
    --sun: #ffe04a;
    --ink: #0b0b0b;
    --flame: #d8281e;
  }
  html, body {
    margin: 0;
    padding: 0;
    overflow: hidden;
    background: var(--paper);
  }
  .poster {
    position: relative;
    width: 849px;
    height: 1200px;
    overflow: hidden;
    background: linear-gradient(to bottom, var(--navy) 0px, #3b43a0 160px, var(--sky) 360px, var(--paper) 540px, var(--paper) 1200px);
    font-family: "Zilla Slab", serif;
    font-weight: 700;
  }
  .artwork {
    position: absolute;
    left: 0;
    top: 160px;
    width: 849px;
    height: 760px;
  }
  .title-banner {
    position: absolute;
    left: 36px;
    top: 58px;
    width: 730px;
    height: 128px;
    background: var(--banner);
    transform: rotate(-3.2deg);
    transform-origin: left top;
    display: flex;
    align-items: center;
    justify-content: center;
  }
  .title {
    margin: 0;
    font-family: "Cabin", sans-serif;
    font-weight: 700;
    font-size: 84px;
    line-height: 1;
    color: var(--sun);
    white-space: nowrap;
  }
  .venue {
    position: absolute;
    left: 216px;
    top: 186px;
    margin: 0;
    font-weight: 700;
    font-size: 52px;
    line-height: 1;
    color: var(--sun);
    transform: rotate(-3.5deg);
    transform-origin: left top;
    white-space: nowrap;
  }
  .details {
    position: absolute;
    left: 168px;
    top: 892px;
    color: var(--ink);
  }
  .details p {
    margin: 0;
    font-weight: 700;
    white-space: nowrap;
  }
  .date, .time {
    font-size: 58px;
    line-height: 72px;
  }
  .organiser {
    font-size: 44px;
    line-height: 68px;
    display: flex;
    align-items: center;
  }
  .organiser-mark {
    display: inline-block;
    width: 36px;
    height: 36px;
    border-radius: 50%;
    background: var(--flame);
    margin: 0 26px 0 22px;
  }
  .social {
    font-size: 27px;
    line-height: 40px;
  }
</style>
</head>
<body>
<main class="poster">
  <svg class="artwork" viewBox="0 0 849 760" role="img" aria-label="Illustration of colourful athlete silhouettes jumping and running over a burst of paint splashes">
    <defs>
      <radialGradient id="burst" cx="50%" cy="50%" r="50%">
        <stop offset="0%" stop-color="#1f9b4a"/>
        <stop offset="30%" stop-color="#2f6fbf"/>
        <stop offset="58%" stop-color="#d8342a"/>
        <stop offset="82%" stop-color="#f7a81b" stop-opacity="0.6"/>
        <stop offset="100%" stop-color="#f7a81b" stop-opacity="0"/>
      </radialGradient>
    </defs>
    <ellipse cx="425" cy="400" rx="420" ry="360" fill="url(#burst)"/>
  </svg>

  <header>
    <div class="title-banner">
      <h1 class="title">KEVO Sports Night</h1>
    </div>
    <p class="venue">Venue: Wendamere Park</p>
  </header>

  <section class="details">
    <p class="date">Date: 25/11/2017</p>
    <p class="time">Time: 4:00pm</p>
    <p class="organiser">Organiser:<span class="organiser-mark"></span>KEVO Sydney</p>
    <p class="social">Friendbook: kevosport</p>
  </section>
</main>
</body>
</html>
```